TWR Business Card Design

As a full service media and advocacy firm, we lean on years of experience in political and corporate consulting, grassroots campaigning, media placement, and video production to deliver unparalleled results. Recently we have moved into digital media and now provide this service for our clients.

I will add our two company logos to be used on the business cards. The longer logo with "sky reach studio" is our primary logo. Our secondary logo is more square one with "sky reach" and 'digital.media.campaigns" on it. We are looking for clean and modern looking business cards fitting for a digital firm.

I will also add our logos that go well with dark backgrounds.

Industry/Entity Type

Political

Contact Information for Business Card

Walter Pennick, Director of Campaigns and Digital, 555-218-4760, walter@skyreachstudioco.example, @SkyReachStudioCo, @WalterPennick, Facebook.com/SkyReachStudioCo

```html
<!DOCTYPE html>
<html lang="en">
<head>
<meta charset="utf-8">
<title>Sky Reach Studio Business Card</title>
<link href="https://fonts.googleapis.com/css2?family=Montserrat:wght@400;500;600&display=swap" rel="stylesheet">
<style>
  :root {
    --backdrop: #3b3b3d;
    --card-dark: #0a0d14;
    --card-light: #ffffff;
    --brand-blue: #1f7fc4;
    --brand-navy: #0d3f8f;
    --ink-white: #ffffff;
  }
  * { margin: 0; padding: 0; box-sizing: border-box; }
  html, body {
    width: 1200px; height: 900px; overflow: hidden;
    background: var(--backdrop);
    font-family: "Montserrat", sans-serif;
  }
  .canvas { position: relative; width: 1200px; height: 900px; }
  .card {
    position: absolute; top: 302px; width: 513px; height: 295px;
    box-shadow: 0 4px 14px rgba(0,0,0,0.45);
  }
  .card-front { left: 73px; background: var(--card-dark); }
  .card-back { left: 616px; background: var(--card-light); }

  .front-wordmark {
    position: absolute; left: 148px; top: 218px;
    display: flex; align-items: center; gap: 10px;
    color: var(--ink-white); font-size: 32px; font-weight: 400;
    letter-spacing: 1px; white-space: nowrap;
  }
  .front-wordmark .mark-dot {
    width: 12px; height: 12px; border-radius: 50%; background: var(--brand-blue);
  }

  .back-wordmark {
    position: absolute; right: 34px; top: 52px;
    display: flex; align-items: center; gap: 8px;
    color: var(--brand-navy); font-size: 30px; font-weight: 600;
    letter-spacing: 0.5px; white-space: nowrap;
  }
  .back-wordmark .mark-dot {
    width: 10px; height: 10px; border-radius: 50%; background: var(--brand-blue);
  }

  .person { position: absolute; left: 48px; top: 154px; right: 34px; }
  .person-name {
    color: var(--brand-blue); font-size: 13px; font-weight: 600; letter-spacing: 0.4px;
  }
  .person-title-row { display: flex; align-items: center; gap: 12px; margin-top: 5px; }
  .person-title { color: var(--brand-navy); font-size: 13px; font-weight: 400; white-space: nowrap; }
  .person-rule { flex: 1; height: 1px; background: var(--brand-navy); }

  .contacts {
    position: absolute; top: 214px; list-style: none;
    color: var(--brand-navy); font-size: 13px; line-height: 20.5px;
  }
  .contacts-main { left: 48px; }
  .contacts-social { left: 345px; }
  .contacts li { display: flex; align-items: center; gap: 6px; white-space: nowrap; }
  .contacts svg { width: 13px; height: 13px; flex: none; }
  .social-dot { width: 12px; height: 12px; border-radius: 50%; background: var(--brand-navy); flex: none; }
</style>
</head>
<body>
<main class="canvas">
  <section class="card card-front">
    <div class="front-wordmark"><span>SKY REACH STUDIO</span><span class="mark-dot"></span></div>
  </section>

  <section class="card card-back">
    <div class="back-wordmark"><span>SKY REACH</span><span class="mark-dot"></span></div>

    <div class="person">
      <p class="person-name">WALTER PENNICK</p>
      <div class="person-title-row">
        <p class="person-title">Director of Campaigns and Digital</p>
        <span class="person-rule"></span>
      </div>
    </div>

    <ul class="contacts contacts-main">
      <li>
        <svg viewBox="0 0 14 14" aria-hidden="true"><circle cx="7" cy="7" r="7" fill="#0d3f8f"/><rect x="4.6" y="3" width="4.8" height="8" rx="1" fill="none" stroke="#fff" stroke-width="1.1"/></svg>
        555-218-4760
      </li>
      <li>
        <svg viewBox="0 0 14 14" aria-hidden="true"><circle cx="7" cy="7" r="7" fill="#0d3f8f"/><rect x="3.5" y="4.5" width="7" height="5" rx="0.6" fill="#fff"/><path d="M3.7 4.8 7 7.4l3.3-2.6" fill="none" stroke="#0d3f8f" stroke-width="0.8"/></svg>
        walter@skyreachstudioco.example
      </li>
      <li>
        <svg viewBox="0 0 14 14" aria-hidden="true"><circle cx="7" cy="7" r="7" fill="#0d3f8f"/><g fill="none" stroke="#fff" stroke-width="0.8"><circle cx="7" cy="7" r="4"/><ellipse cx="7" cy="7" rx="1.8" ry="4"/><path d="M3 7h8"/></g></svg>
        www.skyreachstudioco.example
      </li>
    </ul>

    <ul class="contacts contacts-social">
      <li><span class="social-dot"></span>@SkyReachStudioCo</li>
      <li><span class="social-dot"></span>@WalterPennick</li>
      <li><span class="social-dot"></span>/SkyReachStudioCo</li>
    </ul>
  </section>
</main>
</body>
</html>
```